VORN - Business cards

Business card to be created for Commercial sales staff

Target Market(s)

Commercial businesses

Industry/Entity Type

Commercial

Contact Information for Business Card

Look professional. For commercial clients

Colors
ffffff

Requirements
Must have
• - Vorn Logo
• - Commercial sales staff as postion
• - room for commerical sales manager role
• - person name and their mobile number
• - Website : vornelectrical.com.au
Nice to have
• White background.
• On back of business card just have the logo no other information
Should not have
• Should only have white background on front of card.

```html
<!DOCTYPE html>
<html lang="en">
<head>
<meta charset="utf-8">
<title>VORN – Business Cards</title>
<link rel="stylesheet" href="https://fonts.googleapis.com/css2?family=Arimo:wght@400;700&display=swap">
<style>
  :root {
    --stage: #2b2b2b;
    --card-black: #111114;
    --card-white: #ffffff;
    --brand-red: #c8101a;
    --ink: #1a1a1a;
    --muted: #555555;
  }
  * { box-sizing: border-box; margin: 0; padding: 0; }
  html, body {
    width: 1200px;
    height: 900px;
    overflow: hidden;
    background: var(--stage);
    font-family: "Arimo", Arial, sans-serif;
  }
  .canvas {
    position: relative;
    width: 1200px;
    height: 900px;
  }
  .card {
    position: absolute;
    width: 620px;
    height: 354px;
    border-radius: 22px;
    overflow: hidden;
    box-shadow: 0 14px 30px rgba(0,0,0,0.45);
  }

  /* Back of card */
  .card-back {
    left: 60px;
    top: 90px;
    background: var(--card-black);
    display: flex;
    align-items: center;
    justify-content: center;
  }
  .card-back .wordmark {
    color: var(--card-white);
    font-size: 92px;
  }

  /* Front of card */
  .card-front {
    left: 520px;
    top: 470px;
    background: var(--card-white);
  }
  .wordmark {
    display: flex;
    align-items: center;
    gap: 14px;
    font-weight: 700;
    letter-spacing: 2px;
    line-height: 1;
  }
  .wordmark-dot {
    width: 0.5em;
    height: 0.5em;
    border-radius: 50%;
    background: var(--brand-red);
  }
  .card-front .wordmark {
    position: absolute;
    left: 44px;
    top: 72px;
    color: var(--ink);
    font-size: 64px;
  }
  .person {
    position: absolute;
    right: 36px;
    top: 112px;
    text-align: right;
    line-height: 1.15;
  }
  .person-name {
    color: var(--brand-red);
    font-size: 24px;
    font-weight: 400;
  }
  .person-role {
    color: var(--muted);
    font-size: 13px;
    margin-top: 2px;
  }
  .divider {
    position: absolute;
    left: 30px;
    right: 24px;
    top: 170px;
    height: 1.5px;
    background: var(--brand-red);
  }
  .contact-list {
    position: absolute;
    left: 40px;
    top: 194px;
    list-style: none;
    display: flex;
    flex-direction: column;
    gap: 10px;
  }
  .contact-item {
    display: flex;
    align-items: center;
    gap: 10px;
    color: var(--ink);
    font-size: 17px;
  }
  .contact-item svg {
    width: 16px;
    height: 16px;
    flex: none;
  }
  .band-red {
    position: absolute;
    right: 0;
    bottom: 10px;
    width: 290px;
    height: 22px;
    background: var(--brand-red);
  }
  .band-black {
    position: absolute;
    left: 0;
    right: 0;
    bottom: 0;
    height: 10px;
    background: var(--card-black);
  }
</style>
</head>
<body>
<main class="canvas">

  <section class="card card-back" aria-label="Card back">
    <div class="wordmark"><span class="wordmark-dot"></span><span>VORN</span></div>
  </section>

  <section class="card card-front" aria-label="Card front">
    <div class="wordmark"><span class="wordmark-dot"></span><span>VORN</span></div>

    <div class="person">
      <p class="person-name">Your Name</p>
      <p class="person-role">Postion</p>
    </div>

    <div class="divider"></div>

    <ul class="contact-list">
      <li class="contact-item">
        <svg viewBox="0 0 16 16" aria-hidden="true">
          <circle cx="8" cy="8" r="7" fill="none" stroke="var(--brand-red)" stroke-width="1.6"/>
          <path d="M5.6 4.4l1.3 1.6-.8 1a5 5 0 0 0 2.9 2.9l1-.8 1.6 1.3-.9 1.2C8.3 11.5 4.5 7.7 4.4 5.3z" fill="var(--brand-red)"/>
        </svg>
        <span>88-555-01234</span>
      </li>
      <li class="contact-item">
        <svg viewBox="0 0 16 16" aria-hidden="true">
          <rect x="1" y="3.5" width="14" height="9" fill="var(--brand-red)"/>
          <path d="M1 3.5l7 5 7-5" fill="none" stroke="#fff" stroke-width="1.2"/>
        </svg>
        <span>info@vornelectrical.com.au</span>
      </li>
      <li class="contact-item">
        <svg viewBox="0 0 16 16" aria-hidden="true">
          <g fill="none" stroke="var(--brand-red)" stroke-width="1.3">
            <circle cx="8" cy="8" r="6.5"/>
            <ellipse cx="8" cy="8" rx="2.8" ry="6.5"/>
            <path d="M1.5 8h13M2.5 4.8h11M2.5 11.2h11"/>
          </g>
        </svg>
        <span>www.vornelectrical.com.au</span>
      </li>
    </ul>

    <div class="band-red"></div>
    <div class="band-black"></div>
  </section>

</main>
</body>
</html>
```